Tales from Kin Logo Design plus business cards design

We are a start up company that will help seniors write their memoirs...beginning with a few ancestors and their heritage and continuing through their own history...how they would like to be remembered in the next generation. I envision a card with a senior citizen at an older writing desk, writing her memoirs, with a book (maybe standing on top, leaning slightly) that has the words Tales from Kin.com on the back binding. OR maybe a senior couple walking into the sunset with the same book somewhere in the frame. Communicating the relevance of every life being significant to those that come after them...when a genealogy doesn't say enough about the details of ones life. Please note that I am open to the professionals own ideas...I am not locked into my concepts. On the back of the card I would like one or two phrases..."A Genealogy Doesn't Say Enough" and/or "Every life legacy is uniquely significant to the next generation".
Updates

I have added a couple of photos for ideas that may be used if needed.

I have both increased and committed the payment! Thanks for the reminder!

Reason: We increased the payment commitment and added some photo ideas to help.

We want to thank EVERYONE who participated in this contest. There were so many wonderful and VERY professional proposals...making it very challenging to decide on one! We are posting a new contest for a brochure now and hope many of you will participate. May God bless your endeavors.

Target Market(s)

Senior populous & baby boomer generation.

Industry/Entity Type

Business

Logo Text

Tales from Kin ordinary lives...extraordinary legacy

Requirements
Must have
• Relevant info:
Domain name: talesfromkin.com
email: info@talesfromkin.com
phone: 1-855-GAB-TALE toll free
1-717-382-5619 local
name: Doris Whitlock, M.A.
Nice to have
• photo of senior or senior couple....book with our web address on the binding. I attached two photos that could work if cropped and enhanced. Words need to be deleted from the one photo of senior at a writing desk and couple on the beach could use a sunset sky and other people cropped out. Just ideas...don't know if you have better ones or prefer a different idea.

```html
<!DOCTYPE html>
<html lang="en">
<head>
<meta charset="utf-8">
<title>Tales from Kin — Business Card</title>
<link href="https://fonts.googleapis.com/css2?family=Arimo:wght@400;700&display=swap" rel="stylesheet">
<style>
  :root {
    --canvas-bg: #e6e8ea;
    --front-teal: #0e3b4a;
    --front-band: #0b3341;
    --back-paper: #f5f7f9;
    --ink-navy: #1c2a3a;
    --divider: #7d8791;
    --icon-green: #3fb24a;
    --icon-purple: #8a3ea3;
    --icon-blue: #2a7fc0;
    --white: #ffffff;
  }
  * { box-sizing: border-box; margin: 0; padding: 0; }
  html, body {
    width: 1200px; height: 840px; overflow: hidden;
    background: var(--canvas-bg);
    font-family: "Arimo", Arial, sans-serif;
  }
  .sheet {
    width: 1200px; height: 840px;
    display: flex; align-items: center; justify-content: center; gap: 60px;
  }
  .card {
    position: relative;
    width: 520px; height: 300px;
    border-radius: 22px;
    box-shadow: 0 10px 28px rgba(0,0,0,0.22);
    overflow: hidden;
  }
  /* Front */
  .card-front { background: var(--front-teal); }
  .front-photo {
    position: absolute; left: 78px; top: 134px;
    width: 88px; height: 78px;
    background: linear-gradient(135deg, #3a2416 0%, #7a4a28 45%, #c89a70 80%, #e2d6c8 100%);
  }
  .name-band {
    position: absolute; left: 166px; top: 134px;
    width: 290px; height: 44px;
    background: var(--front-band);
    display: flex; align-items: center; padding-left: 14px;
  }
  .name {
    color: var(--white); font-weight: 700; font-size: 22px; letter-spacing: 0.2px;
    white-space: nowrap;
  }
  /* Back */
  .card-back { background: var(--back-paper); }
  .back-photo {
    position: absolute; left: 104px; top: 92px;
    width: 132px; height: 116px;
    background: linear-gradient(180deg, #b9a99a 0%, #8e7d72 35%, #5a4a40 65%, #3e332c 100%);
  }
  .divider {
    position: absolute; left: 260px; top: 86px;
    width: 1px; height: 128px; background: var(--divider);
  }
  .contact-list {
    position: absolute; left: 272px; top: 92px;
    list-style: none; color: var(--ink-navy); font-size: 14.5px; line-height: 18px;
  }
  .contact-item { display: flex; align-items: flex-start; gap: 6px; }
  .contact-icon {
    flex: none; width: 14px; height: 14px; margin-top: 2px; border-radius: 2px;
    display: flex; align-items: center; justify-content: center;
  }
  .icon-phone { background: var(--icon-green); }
  .icon-email { background: var(--icon-purple); color: var(--white); font-size: 10px; font-weight: 700; line-height: 1; }
  .icon-web { background: var(--icon-blue); }
  .phone-lines span { display: block; }
  .phone-lines .local { padding-left: 8px; }
</style>
</head>
<body>
<main class="sheet">
  <section class="card card-front" aria-label="Business card front">
    <div class="front-photo" role="img" aria-label="Photo of a senior woman writing her memoirs at an old wooden desk"></div>
    <div class="name-band"><span class="name">Doris Whitlock, M.A.</span></div>
  </section>

  <section class="card card-back" aria-label="Business card back">
    <div class="back-photo" role="img" aria-label="Photo of a senior couple walking along a beach at sunset"></div>
    <div class="divider"></div>
    <ul class="contact-list">
      <li class="contact-item">
        <span class="contact-icon icon-phone">
          <svg width="10" height="10" viewBox="0 0 24 24" aria-hidden="true"><path fill="#fff" d="M6.6 10.8a15.1 15.1 0 0 0 6.6 6.6l2.2-2.2a1 1 0 0 1 1-.25 11.4 11.4 0 0 0 3.6.57 1 1 0 0 1 1 1V20a1 1 0 0 1-1 1A17 17 0 0 1 3 4a1 1 0 0 1 1-1h3.5a1 1 0 0 1 1 1c0 1.25.2 2.46.57 3.6a1 1 0 0 1-.25 1z"/></svg>
        </span>
        <span class="phone-lines">
          <span>1-855-GAB-TALE toll free</span>
          <span class="local">1-717-382-5619 local</span>
        </span>
      </li>
      <li class="contact-item">
        <span class="contact-icon icon-email">@</span>
        <span>info@talesfromkin.com</span>
      </li>
      <li class="contact-item">
        <span class="contact-icon icon-web">
          <svg width="10" height="10" viewBox="0 0 24 24" aria-hidden="true" fill="none" stroke="#fff" stroke-width="2"><circle cx="12" cy="12" r="9"/><ellipse cx="12" cy="12" rx="4" ry="9"/><line x1="3" y1="12" x2="21" y2="12"/></svg>
        </span>
        <span>talesfromkin.com</span>
      </li>
    </ul>
  </section>
</main>
</body>
</html>
```